PIETRO business card - High end Italian floors and coverings

We need a new design for our business card. We are an exclusive company located in Mexico.
Our commercial name is PIETRO. Our legal name is Grande Volta SA de CV.
We bring the latest trends in materials for floors and walls such as natural stones, wood, leather, design porcelanato tiles and so.
Our company image colors are black, white and red.
Our customers are high end architects and designers.
We are looking for an elegant but fresh design which reflects exclusivity, simplicity and reliability.
(we are working also in a new website)

Requirements
Nice to have
• back and front design
Space for 2 addresses (one for each showroom location)

```html
<!DOCTYPE html>
<html lang="es">
<head>
<meta charset="utf-8">
<title>PIETRO — Business Card</title>
<link href="https://fonts.googleapis.com/css2?family=Didact+Gothic&family=Montserrat:wght@700&display=swap" rel="stylesheet">
<style>
  :root {
    --stage: #2a2a2b;
    --paper: #f4f4f2;
    --ink: #2b2b2b;
    --ink-soft: #444444;
    --brand-red: #d40f14;
    --rule: #9a9a9a;
    --photo-dark: #1e1d1c;
    --photo-mid: #3a3633;
    --photo-warm: #6b5540;
  }
  * { box-sizing: border-box; margin: 0; padding: 0; }
  html, body {
    width: 1200px; height: 902px; overflow: hidden;
    background: var(--stage);
  }
  .stage {
    position: relative; width: 1200px; height: 902px;
    display: flex; justify-content: center; align-items: center; gap: 60px;
  }
  .card {
    position: relative; width: 380px; height: 665px; overflow: hidden;
    box-shadow: 0 14px 40px rgba(0,0,0,.45);
  }

  /* Front */
  .card--front { background: var(--photo-dark); }
  .front__photo {
    position: absolute; inset: 0;
    background: linear-gradient(170deg, var(--photo-mid) 0%, var(--photo-dark) 45%, #2c2724 70%, var(--photo-warm) 100%);
  }
  .wordmark {
    position: absolute; display: flex; align-items: center; gap: 14px;
    font-family: "Didact Gothic", sans-serif; letter-spacing: 4px;
  }
  .wordmark__square { width: 22px; height: 22px; background: var(--brand-red); flex: none; }
  .card--front .wordmark { top: 58px; left: 40px; font-size: 50px; color: #ffffff; }

  /* Back */
  .card--back { background: var(--paper); color: var(--ink); font-family: "Didact Gothic", sans-serif; }
  .card--back .wordmark { top: 58px; left: 40px; font-size: 50px; color: var(--ink); }
  .contact { position: absolute; top: 200px; left: 40px; right: 34px; }
  .contact__name {
    font-family: "Montserrat", sans-serif; font-weight: 700;
    font-size: 17px; letter-spacing: 1.5px; text-transform: uppercase;
  }
  .contact__line { font-size: 15px; line-height: 1.55; color: var(--ink-soft); }
  .label { color: var(--brand-red); }
  .showroom { border-top: 1px solid var(--rule); margin-top: 26px; padding-top: 20px; }
  .showroom--last { border-bottom: 1px solid var(--rule); padding-bottom: 22px; }
</style>
</head>
<body>
<main class="stage">
  <section class="card card--front" aria-label="Card front">
    <div class="front__photo" role="img" aria-label="Interior photograph: dark stone-clad wall with a fireplace, leather armchair and sofa with green cushion"></div>
    <div class="wordmark"><span class="wordmark__square"></span>PIETRO</div>
  </section>

  <section class="card card--back" aria-label="Card back">
    <div class="wordmark"><span class="wordmark__square"></span>PIETRO</div>
    <div class="contact">
      <p class="contact__name">Carla Benetti Ruiz</p>
      <p class="contact__line"><span class="label">Email:</span> carla@pietro.com.mx</p>

      <div class="showroom">
        <p class="contact__line">Cristal #1820 Esq. Navarra</p>
        <p class="contact__line">Colonia Arcos CP 44130</p>
        <p class="contact__line">Guadalajara, Jalisco</p>
        <p class="contact__line"><span class="label">Tel:</span> (33) 355.210.48</p>
      </div>

      <div class="showroom showroom--last">
        <p class="contact__line">Lago Pátzcuaro #215</p>
        <p class="contact__line">Local B 2do, Colonia Granada</p>
        <p class="contact__line">CP 11520, Mexico, DF</p>
        <p class="contact__line"><span class="label">Tel:</span> (33) 548.102.63</p>
      </div>
    </div>
  </section>
</main>
</body>
</html>
```